Indianapolis based store looking for a multi-page website, to include ecommerce. We sell Heron mattresses, which are manufactured in Fort Wayne, Indiana. The design line of mattresses includes the blue heron (value), white heron (mid-value) and night heron (high end). We also offer mattresses for RV, futon and pet mattresses. We want a user-friendly website with e-commerce capability. Web pages should include pictures of our product, bio/history of operator/Heron cooperation, detailed description of the product, shopping cart. Paypal, major credit cards accepted.

Facts about the store: 4127 N. Larkdale Rd Suite 260 Indianapolis, IN 46219 #317-555-0182. Domain name we would like is www.slumbernook.example. If this domain is already taken, we would like www.slumbernook-shop.example. Features that set Slumber Nook apart from competitors: local delivery within a day, product stored on site and available to take home the same day, vacuumed sealed boxed option for same day take home, dual-sided mattress options (firm/plush), locally owned/operated, locally manufactured (Fort Wayne, IN), FoamVeri-CA certified (info link for FoamVeri https://foamveri.example/ )

Here is the website we will be using for background information/pictures. Please check out the descriptions/pictures for ideas. We are waiting to hear back from Heron's owners in regard to permission using their actual photos.

https://www.heronbeds.example/products/mattresses/

https://www.heronbeds.example/products/futons/

We will be attaching a price list. We will probably have more products/info to add. We are also attaching our logo which was designed with Artisan Hive but we need to get a higher res copy from the designer.

We also would like an email associated with the website/company: info@slumbernook.example ( we are not sure how an email gets set up)

Target Market(s)

mattress shoppers!

Industry/Entity Type

Retail

Coding

Coded - Design and coding required

Number of Pages Required

5+ page

Font styles to use
Sans Serif

Colors
0455a3
cfdeed
eaf1f7

Requirements
Must have
• e-commerce/shopping cart, pictures (pets in beds, RVs, futons etc - please see websites listed in project description), watermark, user friendly, product information (please see web site listed in project description), crisp pictures/lines, should emote a sense of comfort, ability to be viewed on mobile device
• link to follow on FB/IG https://www.facebook.com/slumbernook/ IG: slumbernook
• ability for the customer/viewer to "contact us now/ask questions". Ability for customers to leave reviews on products/star rating
• prices should be listed next to product, not "see price in cart", ability to "sort" by price low-high, filter options (i.e. type: pet, RV, futon, mattress,) then a filter option for mattress size (twin, full, queen, king)
Should not have
• rollover/mouse over

```html
<!DOCTYPE html>
<html lang="en">
<head>
<meta charset="utf-8">
<title>Slumber Nook</title>
<link href="https://fonts.googleapis.com/css2?family=Quicksand:wght@400;500;600;700&display=swap" rel="stylesheet">
<style>
:root{
  --blue:#0455a3;
  --blue-dark:#033f7c;
  --sky:#1ea0e6;
  --light:#cfdeed;
  --pale:#eaf1f7;
  --panel:#f4f6f9;
  --ink:#1d2b3a;
  --muted:#6d7a88;
  --red:#d8262d;
  --gold:#f3b51b;
  --white:#ffffff;
}
*{box-sizing:border-box;margin:0;padding:0}
html,body{width:1200px;height:4986px;overflow:hidden}
body{position:relative;background:var(--white);font-family:"Quicksand",sans-serif;color:var(--ink)}
.abs{position:absolute}
.btn{display:inline-block;border-radius:20px;font-weight:700;font-size:13px;padding:8px 22px;text-align:center;white-space:nowrap}
.btn-solid{background:var(--blue);color:var(--white)}
.btn-ghost{border:1.5px solid var(--blue);color:var(--blue);background:var(--white)}
.section-title{position:absolute;left:0;width:1200px;text-align:center;color:var(--blue);font-size:36px;font-weight:600}
.section-sub{position:absolute;left:0;width:1200px;text-align:center;color:var(--muted);font-size:13px}
.photo{position:absolute}

/* top bar + nav */
.topbar{top:0;left:0;width:1200px;height:28px;background:var(--pale);font-size:12px;color:var(--ink)}
.topbar .contact{left:90px;top:7px}
.topbar .contact b{color:var(--blue)}
.topbar .account{left:715px;top:7px}
.topbar .search{left:875px;top:3px;width:235px;height:22px;border-radius:11px;background:var(--white);border:1px solid var(--light);padding:3px 12px;color:var(--muted);font-size:11px}
.header{top:28px;left:0;width:1200px;height:97px;background:var(--white)}
.logo{left:90px;top:30px}
.logo .name{font-size:32px;font-weight:700;color:var(--blue);letter-spacing:1px;line-height:1}
.menu{left:470px;top:42px;display:flex;gap:40px;font-size:14px;font-weight:600}
.menu .active{color:var(--blue)}
.cart{left:935px;top:37px;width:26px;height:26px;border-radius:50%;border:1.5px solid var(--blue)}
.header .btn{left:985px;top:36px;padding:6px 22px}

/* hero */
.hero{top:125px;left:0;width:1200px;height:560px;overflow:hidden}
.hero .photo{inset:0;background:linear-gradient(100deg,#f2f3f3 0%,#e6e7e6 45%,#d4d6d5 70%,#ecedec 100%)}
.hero h1{left:90px;top:135px;font-size:36px;color:var(--blue);font-weight:600}
.hero p{left:90px;top:180px;font-size:13px;color:var(--ink)}
.hero .btn{left:90px;top:212px}
.hero svg{position:absolute;left:0;bottom:0}

/* story */
.story h2{left:90px;top:748px;font-size:36px;color:var(--blue);font-weight:600}
.story .copy{left:90px;top:820px;width:440px;font-size:13px;line-height:1.6;color:var(--ink)}
.story .copy p{margin-bottom:14px}
.story .btn{left:90px;top:1045px}
.diamond{position:absolute;width:150px;height:150px;transform:rotate(45deg)}

/* collections */
.band{left:0;top:1420px;width:1200px;height:150px;background:var(--pale)}
.coll-card{position:absolute;top:1272px;width:320px;height:264px;background:var(--light);overflow:hidden}
.coll-card.raised{background:var(--white);box-shadow:0 8px 24px rgba(4,85,163,.18)}
.coll-card .photo{left:0;top:40px;width:170px;height:150px}
.coll-card .brand{position:absolute;right:16px;top:26px;display:flex;align-items:center;gap:8px;font-size:20px;font-weight:700;line-height:1.05;text-align:right;color:#8c9299}
.coll-card .brand i{display:block;width:30px;height:30px;border-radius:50%;background:#8c9299}
.coll-card .label{position:absolute;left:0;width:100%;top:198px;text-align:center;font-size:13px;font-weight:700}
.coll-card .btn{position:absolute;right:28px;top:224px;padding:5px 18px;font-size:12px}

/* promise */
.promise{left:90px;top:1629px;width:1020px;height:282px;background:var(--panel);text-align:center}
.promise .icon{position:absolute;left:484px;top:52px}
.promise h3{position:absolute;top:140px;width:100%;font-size:26px;color:var(--blue);font-weight:600}
.promise p{position:absolute;top:184px;width:100%;font-size:12px;color:var(--muted);line-height:1.6}
.feature{position:absolute;top:1928px;height:133px;background:var(--panel);display:flex;align-items:center;gap:18px;padding-left:40px;font-size:15px;font-weight:600;color:var(--blue);line-height:1.35}

/* products */
.prod-band{left:0;top:2390px;width:1200px;height:340px;background:var(--panel)}
.tabs{left:378px;top:2196px;width:444px;height:32px;border:1.5px solid var(--light);border-radius:16px;display:flex;font-size:12px;font-weight:600;overflow:hidden}
.tabs span{flex:1;display:flex;align-items:center;justify-content:center}
.tabs .on{background:var(--blue);color:var(--white);border-radius:16px}
.prod{position:absolute;top:2290px;width:300px;height:400px;padding:0}
.prod.raised{background:var(--white);box-shadow:0 8px 26px rgba(0,0,0,.13);top:2276px;height:446px;padding:14px}
.prod .photo{position:relative;width:100%;height:230px}
.prod h4{font-size:14px;margin-top:16px;font-weight:700}
.prod .desc{font-size:11px;color:var(--muted);margin-top:6px;line-height:1.45}
.prod .price{display:flex;align-items:center;gap:10px;margin-top:10px;font-size:15px;font-weight:700;color:var(--red)}
.prod .price s{color:var(--muted);font-weight:500;font-size:13px}
.prod .price .stars{margin-left:auto;color:var(--gold);font-size:14px;letter-spacing:1px}
.prod .btn{margin-top:14px;padding:6px 16px;font-size:12px}
.arrow{position:absolute;font-size:22px;color:var(--muted)}

/* newsletter */
.news-input{left:370px;top:2963px;width:350px;height:38px;border-bottom:1.5px solid var(--light);font-size:12px;color:var(--muted);padding:12px 8px}
.news-btn{left:722px;top:2963px;width:112px;height:38px;border-radius:20px;background:var(--blue);color:var(--white);font-size:13px;font-weight:700;text-align:center;line-height:38px}

/* reviews */
.review{left:210px;top:3324px;width:780px;height:300px;background:var(--white);box-shadow:0 8px 30px rgba(0,0,0,.1);overflow:hidden;text-align:center}
.review h5{position:absolute;top:42px;width:100%;font-size:18px;color:var(--ink);font-weight:600}
.review .stars{position:absolute;top:70px;width:100%;color:var(--gold);font-size:14px;letter-spacing:2px}
.review p{position:absolute;top:110px;left:120px;width:540px;font-size:13px;line-height:1.6;color:var(--muted)}
.review p b{color:var(--blue);font-size:18px}
.review .who{position:absolute;top:200px;width:100%;font-size:13px;font-weight:700;color:var(--blue)}
.dots{position:absolute;top:240px;width:100%;display:flex;justify-content:center;gap:6px}
.dots i{width:9px;height:9px;border-radius:50%;border:1.5px solid var(--muted)}

/* posts */
.post-title{font-size:17px;font-weight:600;line-height:1.35;color:var(--ink)}
.post-text{font-size:12px;color:var(--muted);line-height:1.6;margin-top:10px}
.read{font-size:12px;font-weight:700;color:var(--blue);margin-top:8px}

/* footer */
.footer{left:0;top:4437px;width:1200px;height:549px;overflow:hidden;color:var(--white)}
.footer .bg{position:absolute;inset:0}
.footer .logo{left:90px;top:160px}
.footer .logo .name{color:var(--white)}
.footer .info{left:90px;top:215px;font-size:13px;line-height:1.7}
.footer .info .call{font-size:20px;font-weight:700}
.social{left:90px;top:345px;display:flex;gap:10px}
.social i{width:24px;height:24px;border-radius:50%;border:1.5px solid var(--white)}
.footer h6{font-size:15px;font-weight:700}
.links{left:420px;top:160px}
.links ul{list-style:none;margin-top:20px;font-size:13px;line-height:2}
.form{left:590px;top:160px;width:520px}
.field{height:28px;background:rgba(255,255,255,.12);border:1px solid rgba(255,255,255,.35);font-size:12px;padding:6px 10px}
.fine{left:90px;top:490px;width:1020px;display:flex;align-items:center;font-size:12px;gap:30px}
.cards{margin-left:auto;display:flex;gap:8px}
.cards i{width:40px;height:24px;border-radius:4px;background:var(--white)}
</style>
</head>
<body>

<div class="abs topbar">
  <div class="abs contact"><b>Call:</b> 317-555-0182 &nbsp;&nbsp; <b>Email:</b> info@slumbernook.example</div>
  <div class="abs account">Login / Sign Up</div>
  <div class="abs search">Search Here ...</div>
</div>

<header class="abs header">
  <div class="abs logo"><div class="name">SLUMBER NOOK</div></div>
  <nav class="abs menu"><span class="active">Home</span><span>Our Story</span><span>Products ▾</span><span>Review</span><span>Blog</span></nav>
  <div class="abs cart"></div>
  <span class="abs btn btn-ghost">Contact Us</span>
</header>

<section class="abs hero">
  <div class="photo" role="img" aria-label="Woman relaxing on a white bed in a bright bedroom with framed art and a wall clock"></div>
  <h1 class="abs">It's Bedtime.</h1>
  <p class="abs">Explore sleep solutions that work like a dream.</p>
  <span class="abs btn btn-solid">Shop Now!</span>
  <svg width="1200" height="110" viewBox="0 0 1200 110" aria-hidden="true">
    <path d="M0 80 C300 10 700 10 1200 40 L1200 110 L0 110Z" fill="#fff"/>
    <path d="M0 80 C300 10 700 10 1200 40" fill="none" stroke="var(--blue)" stroke-width="6"/>
  </svg>
</section>

<section class="story">
  <h2 class="abs">Our Story</h2>
  <div class="abs copy">
    <p>Slumber Nook was founded by two bright partners looking to build their vision of dependable customer service and quality products under one roof. After working in retail for a combined 20+ years, Slumber Nook's founders wanted to put their knowledge, skill and experience to work for themselves.</p>
    <p>After researching many fine makers to showcase in their store, Heron mattresses stood out for both its comfort and quality, so we mention its sleek design ...</p>
  </div>
  <span class="abs btn btn-ghost">Discover More</span>
  <div class="diamond" style="left:808px;top:750px;background:linear-gradient(135deg,#f4f4f2,#c9ccd0)" role="img" aria-label="Bedroom with mattress and pillows"></div>
  <div class="diamond" style="left:720px;top:862px;background:linear-gradient(135deg,#e9e5df,#b7b0a6)" role="img" aria-label="Mattress in a furnished bedroom"></div>
  <div class="diamond" style="left:896px;top:862px;background:linear-gradient(135deg,#eef0f2,#a9b1ba)" role="img" aria-label="Close view of a mattress corner"></div>
  <div class="diamond" style="left:808px;top:960px;background:linear-gradient(135deg,#5a5550,#25221f)" role="img" aria-label="Dark mattress on a bed frame"></div>
</section>

<h2 class="section-title" style="top:1190px">Mattress Collections</h2>
<div class="abs band"></div>
<svg class="abs" style="left:0;top:1420px" width="1200" height="90" viewBox="0 0 1200 90" aria-hidden="true">
  <path d="M0 60 C250 90 600 0 1200 20" fill="none" stroke="var(--sky)" stroke-width="5"/>
</svg>
<div class="coll-card" style="left:90px">
  <div class="photo" role="img" aria-label="Gray quilted mattress" style="background:linear-gradient(160deg,#b9bcc0,#7e838a)"></div>
  <div class="brand">BLUE<br>HERON<i></i></div>
  <div class="label">Blue Heron Collections</div>
  <span class="btn btn-ghost">Shop Now!</span>
</div>
<div class="coll-card raised" style="left:440px">
  <div class="photo" role="img" aria-label="Silver quilted mattress" style="background:linear-gradient(160deg,#d3d6da,#8c9198)"></div>
  <div class="brand">WHITE<br>HERON<i></i></div>
  <div class="label">White Heron Collections</div>
  <span class="btn btn-solid">Shop Now!</span>
</div>
<div class="coll-card" style="left:790px">
  <div class="photo" role="img" aria-label="Black quilted mattress" style="background:linear-gradient(160deg,#5b5f66,#1f2226)"></div>
  <div class="brand" style="color:#1f2226">NIGHT<br>HERON<i style="background:#1f2226"></i></div>
  <div class="label">Night Heron Collections</div>
  <span class="btn btn-ghost">Shop Now!</span>
</div>

<div class="abs promise">
  <svg class="icon" width="52" height="52" viewBox="0 0 52 52" aria-hidden="true">
    <rect x="8" y="8" width="36" height="36" rx="4" fill="none" stroke="var(--blue)" stroke-width="2.5"/>
    <line x1="8" y1="18" x2="44" y2="18" stroke="var(--blue)" stroke-width="2.5"/>
    <rect x="15" y="24" width="6" height="6" fill="var(--blue)"/><rect x="24" y="24" width="6" height="6" fill="var(--blue)"/><rect x="33" y="24" width="6" height="6" fill="var(--blue)"/>
    <rect x="15" y="33" width="6" height="6" fill="var(--blue)"/><rect x="24" y="33" width="6" height="6" fill="var(--blue)"/>
  </svg>
  <h3>100 Day Slumber Nook Promise</h3>
  <p>Try out our mattresses for 100 days. If you're not happy,<br>we'll take it back — no questions asked.</p>
</div>
<div class="feature" style="left:90px;width:330px">
  <svg width="40" height="40" viewBox="0 0 40 40" aria-hidden="true"><circle cx="20" cy="22" r="14" fill="none" stroke="var(--blue)" stroke-width="2.5"/><path d="M14 6h12l-3 5h-6z" fill="none" stroke="var(--blue)" stroke-width="2"/><text x="20" y="27" text-anchor="middle" font-size="14" font-weight="700" fill="var(--blue)" font-family="Quicksand,sans-serif">$</text></svg>
  <span>No Budget? No Problem.<br>Available at 0% EMI</span>
</div>
<div class="feature" style="left:437px;width:326px">
  <svg width="40" height="40" viewBox="0 0 40 40" aria-hidden="true"><path d="M20 4l13 5v10c0 9-6 14-13 17C13 33 7 28 7 19V9z" fill="none" stroke="var(--blue)" stroke-width="2.5"/><path d="M14 20l4 4 8-9" fill="none" stroke="var(--blue)" stroke-width="2.5"/></svg>
  <span>Sleep worry free with<br>10 year warranty</span>
</div>
<div class="feature" style="left:780px;width:330px">
  <svg width="44" height="40" viewBox="0 0 44 40" aria-hidden="true"><rect x="3" y="10" width="24" height="18" fill="none" stroke="var(--blue)" stroke-width="2.5"/><path d="M27 15h8l6 7v6H27z" fill="none" stroke="var(--blue)" stroke-width="2.5"/><circle cx="12" cy="31" r="4" fill="#fff" stroke="var(--blue)" stroke-width="2.5"/><circle cx="33" cy="31" r="4" fill="#fff" stroke="var(--blue)" stroke-width="2.5"/></svg>
  <span>Free shipping &amp; cash<br>on delivery</span>
</div>

<h2 class="section-title" style="top:2125px">Featured Products</h2>
<div class="abs prod-band"></div>
<div class="abs tabs"><span class="on">Mattress</span><span>Pet Mattress</span><span>Swivel RV's</span><span>Futon</span></div>
<span class="arrow" style="left:8px;top:2380px">‹</span>
<span class="arrow" style="left:1180px;top:2380px">›</span>
<div class="prod" style="left:100px">
  <div class="photo" role="img" aria-label="Mattress on a black bed frame in a bright room" style="background:linear-gradient(170deg,#eef0f2,#9aa3ad)"></div>
  <h4>Lorem Ipsum Mattress</h4>
  <div class="desc">There are many variations of passages of<br>plush layered foam available...</div>
  <div class="price">$1200 <s>$1400</s><span class="stars">★★★★★</span></div>
  <span class="btn btn-ghost">Shop Now!</span>
</div>
<div class="prod raised" style="left:445px">
  <div class="photo" role="img" aria-label="Mattress on a black bed frame against a brick wall" style="background:linear-gradient(170deg,#a58c78,#4d4440)"></div>
  <h4>Lorem Ipsum Mattress</h4>
  <div class="desc">There are many variations of passages of<br>plush layered foam available...</div>
  <div class="price">$1200 <s>$1400</s><span class="stars">★★★★★</span></div>
  <span class="btn btn-solid">Shop Now!</span>
</div>
<div class="prod" style="left:800px">
  <div class="photo" role="img" aria-label="Dark mattress on a bed frame beside a plant" style="background:linear-gradient(170deg,#e6e8ea,#525a66)"></div>
  <h4>Lorem Ipsum Mattress</h4>
  <div class="desc">There are many variations of passages of<br>plush layered foam available...</div>
  <div class="price">$1200 <s>$1400</s><span class="stars">★★★★★</span></div>
  <span class="btn btn-ghost">Shop Now!</span>
</div>
<span class="abs btn btn-ghost" style="left:520px;top:2760px;padding:5px 18px;font-size:12px">View All Products</span>

<h2 class="section-title" style="top:2860px">Before You Sleep</h2>
<div class="section-sub" style="top:2915px">Sign up to our newsletter to get the latest on offers, new releases and more!</div>
<div class="abs news-input">Enter your email...</div>
<div class="abs news-btn">Subscribe</div>
<svg class="abs" style="left:0;top:3060px" width="1200" height="80" viewBox="0 0 1200 80" aria-hidden="true">
  <path d="M0 30 C300 70 700 0 1200 30" fill="none" stroke="var(--blue)" stroke-width="6"/>
  <path d="M0 42 C300 82 700 12 1200 42" fill="none" stroke="var(--sky)" stroke-width="2"/>
</svg>

<h2 class="section-title" style="top:3220px">Sleep Talking</h2>
<div class="section-sub" style="top:3275px">Words of praise and love from our customers.</div>
<span class="arrow" style="left:140px;top:3450px">‹</span>
<span class="arrow" style="left:1050px;top:3450px">›</span>
<div class="abs review">
  <svg class="abs" style="right:0;top:0" width="150" height="80" viewBox="0 0 150 80" aria-hidden="true"><path d="M20 0H150V80C110 60 60 40 20 0Z" fill="var(--sky)"/></svg>
  <svg class="abs" style="left:0;bottom:0" width="150" height="80" viewBox="0 0 150 80" aria-hidden="true"><path d="M0 0C40 40 90 60 130 80H0Z" fill="var(--sky)"/></svg>
  <h5>Love This Mattress</h5>
  <div class="stars">★★★★★</div>
  <p><b>“</b> Lorem ipsum is simply dummy text of the printing and quilting typesetting industry. Lorem ipsum has been the industry's standard dummy text but the majority have suffered alteration in some form, by injected. <b>”</b></p>
  <div class="who">Dana Whitfield</div>
  <div class="dots"><i></i><i></i><i style="background:var(--muted)"></i><i></i><i></i></div>
</div>
<span class="abs btn btn-ghost" style="left:430px;top:3660px;padding:5px 18px;font-size:12px">View All Review</span>
<span class="abs btn btn-ghost" style="left:605px;top:3660px;padding:5px 18px;font-size:12px">Leave Your Review</span>

<h2 class="section-title" style="top:3760px">Recent Posts</h2>
<div class="photo" style="left:90px;top:3839px;width:493px;height:280px;background:linear-gradient(160deg,#e9ecef,#aeb6bf)" role="img" aria-label="Living room with a gray sofa and framed pictures"></div>
<div class="abs" style="left:90px;top:4150px;width:493px">
  <div class="post-title">There are many variations of passages Lorem</div>
  <div class="post-text">Lorem ipsum is simply dummy text of the printing and typesetting industry. Lorem ipsum has been the industry's standard dummy text ever since the 1500s, when an unknown.</div>
  <div class="read">Read More ›</div>
</div>
<div class="photo" style="left:615px;top:3839px;width:230px;height:200px;background:linear-gradient(160deg,#e4ddd3,#9d8f80)" role="img" aria-label="Person resting on a bed"></div>
<div class="abs" style="left:875px;top:3855px;width:235px">
  <div class="post-title">There are many variations of passages Lorem</div>
  <div class="post-text">Lorem ipsum is simply dummy text of the printing and typesetting industry. Lorem has been the industry's...</div>
  <div class="read">Read More ›</div>
</div>
<div class="photo" style="left:615px;top:4070px;width:230px;height:210px;background:linear-gradient(160deg,#f1efec,#b9b2a8)" role="img" aria-label="Person jumping on a bed in a bright room"></div>
<div class="abs" style="left:875px;top:4090px;width:235px">
  <div class="post-title">There are many variations of passages Lorem</div>
  <div class="post-text">Lorem ipsum is simply dummy text of the printing and typesetting industry. Lorem has been the industry's...</div>
  <div class="read">Read More ›</div>
</div>
<span class="abs btn btn-ghost" style="left:518px;top:4310px;padding:5px 22px;font-size:12px">View All Blog</span>

<footer class="abs footer">
  <svg class="bg" width="1200" height="549" viewBox="0 0 1200 549" aria-hidden="true">
    <defs><linearGradient id="foot" x1="0" y1="0" x2="0" y2="1"><stop offset="0" stop-color="#0a67bf"/><stop offset="1" stop-color="#033f7c"/></linearGradient></defs>
    <path d="M0 70 C300 10 800 120 1200 30 V549 H0Z" fill="url(#foot)"/>
    <path d="M0 60 C300 0 800 110 1200 20" fill="none" stroke="var(--sky)" stroke-width="4"/>
    <line x1="90" y1="470" x2="1110" y2="470" stroke="rgba(255,255,255,.3)"/>
  </svg>
  <div class="abs logo"><div class="name">SLUMBER NOOK</div></div>
  <div class="abs info">
    <div class="call">Call: +123 - 456 - 7890</div>
    <div>info@slumbernook.example</div>
    <div style="margin-top:10px">4127 N. Larkdale Rd Suite 260 Indianapolis,<br>IN 46219</div>
  </div>
  <div class="abs social"><i></i><i></i><i></i></div>
  <div class="abs links">
    <h6>Quick Links</h6>
    <ul><li>Home</li><li>Our Story</li><li>Products</li><li>Review</li><li>Blog</li><li>Contact Us</li></ul>
  </div>
  <div class="abs form">
    <h6>Send Us a Message</h6>
    <div style="display:flex;gap:10px;margin-top:20px">
      <div class="field" style="flex:1">Name</div><div class="field" style="flex:1">Phone</div><div class="field" style="flex:1">Email</div>
    </div>
    <div class="field" style="height:92px;margin-top:10px;position:relative">Message ...
      <span style="position:absolute;right:8px;bottom:-12px;width:26px;height:26px;border-radius:50%;background:var(--sky)"></span>
    </div>
  </div>
  <svg class="abs" style="left:1098px;top:160px" width="14" height="12" viewBox="0 0 14 12" aria-hidden="true"><path d="M1 11L7 1l6 10" fill="none" stroke="var(--sky)" stroke-width="2"/></svg>
  <div class="abs fine">
    <span>© 2019 Slumber Nook. All Rights Reserved</span><span>Privacy Policy</span><span>Terms &amp; Conditions</span>
    <span class="cards"><i></i><i></i><i></i><i></i><i></i></span>
  </div>
</footer>

</body>
</html>
```